Design Business Card for use in pressly cards

I have a logo and a unfinished website for reference to develop a business card

http://brightquill.com.au/dev/brightquill/

```html
<!DOCTYPE html>
<html lang="en">
<head>
<meta charset="UTF-8">
<title>Bright Quill — Business Card</title>
<link rel="stylesheet" href="https://fonts.googleapis.com/css2?family=Lato:wght@400;700&display=swap">
<style>
  :root {
    --stage: #dcdcdc;
    --stage-light: #f2f2f2;
    --card-white: #ffffff;
    --slate: #5f5f61;
    --orange: #ef5a24;
    --text-light: #ffffff;
    --shadow: rgba(0, 0, 0, 0.28);
  }
  * { margin: 0; padding: 0; box-sizing: border-box; }
  html, body {
    width: 1200px;
    height: 1200px;
    overflow: hidden;
  }
  body {
    background: radial-gradient(circle at 50% 45%, var(--stage-light) 0%, var(--stage) 75%);
    font-family: 'Lato', sans-serif;
    position: relative;
  }
  .card {
    position: absolute;
    width: 700px;
    height: 400px;
    background: var(--card-white);
    box-shadow: 0 10px 30px var(--shadow);
    overflow: hidden;
  }
  .card--front { left: 250px; top: 150px; }
  .card--back  { left: 250px; top: 650px; }

  .card__shapes {
    position: absolute;
    inset: 0;
    width: 100%;
    height: 100%;
  }

  .brand {
    position: absolute;
    display: flex;
    align-items: center;
    gap: 12px;
    color: var(--orange);
    font-weight: 700;
    font-size: 32px;
    white-space: nowrap;
  }
  .brand__dot {
    width: 18px;
    height: 18px;
    border-radius: 50%;
    background: var(--orange);
  }
  .card--front .brand { left: 38px; top: 178px; }
  .card--back .brand { left: 50%; top: 130px; transform: translateX(-50%); font-size: 40px; }

  .identity {
    position: absolute;
    left: 368px;
    top: 52px;
  }
  .identity__name {
    color: var(--orange);
    font-size: 34px;
    font-weight: 400;
    line-height: 1.1;
  }
  .identity__role {
    color: var(--text-light);
    font-size: 26px;
    font-weight: 400;
    margin-top: 4px;
  }

  .contacts {
    position: absolute;
    left: 368px;
    top: 158px;
    list-style: none;
  }
  .contacts__item {
    display: flex;
    align-items: center;
    gap: 16px;
    height: 45px;
    color: var(--text-light);
    font-size: 20px;
  }
  .contacts__icon {
    width: 24px;
    height: 24px;
    flex: none;
    fill: var(--orange);
  }

  .band {
    position: absolute;
    left: 0;
    right: 0;
    bottom: 24px;
    height: 74px;
    background: var(--orange);
    color: var(--text-light);
    font-size: 34px;
    display: flex;
    align-items: center;
    justify-content: center;
    letter-spacing: 0.5px;
  }
</style>
</head>
<body>

  <section class="card card--front" aria-label="Business card front">
    <svg class="card__shapes" viewBox="0 0 700 400" aria-hidden="true">
      <path d="M300,0 Q195,200 320,400 L700,400 L700,0 Z" fill="var(--slate)"/>
      <path d="M290,0 Q185,200 310,400" fill="none" stroke="var(--orange)" stroke-width="6"/>
    </svg>

    <div class="brand"><span class="brand__dot"></span>Bright Quill</div>

    <div class="identity">
      <h1 class="identity__name">Mara Quinlan</h1>
      <p class="identity__role">President</p>
    </div>

    <ul class="contacts">
      <li class="contacts__item">
        <svg class="contacts__icon" viewBox="0 0 24 24" aria-hidden="true"><path d="M6.6 10.8c1.4 2.8 3.8 5.1 6.6 6.6l2.2-2.2c.3-.3.7-.4 1-.2 1.1.4 2.3.6 3.6.6.6 0 1 .4 1 1V20c0 .6-.4 1-1 1C10.6 21 3 13.4 3 4c0-.6.4-1 1-1h3.5c.6 0 1 .4 1 1 0 1.3.2 2.5.6 3.6.1.3 0 .7-.2 1z"/></svg>
        <span>1-555-014-2297</span>
      </li>
      <li class="contacts__item">
        <svg class="contacts__icon" viewBox="0 0 24 24" aria-hidden="true"><path d="M12 2a10 10 0 1 0 0 20 10 10 0 0 0 0-20zm6.9 6h-3a15 15 0 0 0-1.3-3.9A8 8 0 0 1 18.9 8zM12 4c.8 1.2 1.5 2.5 1.9 4h-3.8c.4-1.5 1.1-2.8 1.9-4zM4.3 14a8 8 0 0 1 0-4h3.4a16 16 0 0 0 0 4zm.8 2h3a15 15 0 0 0 1.3 3.9A8 8 0 0 1 5.1 16zm3-8h-3a8 8 0 0 1 4.3-3.9C8.8 5.3 8.4 6.6 8.1 8zM12 20c-.8-1.2-1.5-2.5-1.9-4h3.8c-.4 1.5-1.1 2.8-1.9 4zm2.3-6H9.7a14 14 0 0 1 0-4h4.6a14 14 0 0 1 0 4zm.3 5.9c.6-1.2 1-2.5 1.3-3.9h3a8 8 0 0 1-4.3 3.9zm1.7-5.9a16 16 0 0 0 0-4h3.4a8 8 0 0 1 0 4z"/></svg>
        <span>www.brightquill.com.au</span>
      </li>
      <li class="contacts__item">
        <svg class="contacts__icon" viewBox="0 0 24 24" aria-hidden="true"><path d="M3 5h18v14H3zm2 2v.5l7 5 7-5V7l-7 5z"/></svg>
        <span>hello@brightquill.com.au</span>
      </li>
      <li class="contacts__item">
        <svg class="contacts__icon" viewBox="0 0 24 24" aria-hidden="true"><path d="M12 2a7 7 0 0 0-7 7c0 5.2 7 13 7 13s7-7.8 7-13a7 7 0 0 0-7-7zm0 9.5a2.5 2.5 0 1 1 0-5 2.5 2.5 0 0 1 0 5z"/></svg>
        <span>Street Address Here, Australia</span>
      </li>
    </ul>
  </section>

  <section class="card card--back" aria-label="Business card back">
    <div class="brand"><span class="brand__dot"></span>Bright Quill</div>
    <div class="band">www.brightquill.com.au</div>
  </section>

</body>
</html>
```